Ferncrest Dental, LLC business card project

Business card to be designed with current logo.
Dental office- please keep design of card that looks clean and professional.
Please include the following info:
Ferncrest Dental, LLC
Dr. Lorna Pettigrew
2871 Marlowe Street
Bethlehem, PA 18093
610-555-0193
ferncrestdental.office@examplemail.test
Hello everyone-
Reason: Just got back from overseas- will look at all designs and provide feedback. Thank you!
Reason: Polling my friends for the final selection-
thank you to all those that participated- so many talented designers!

```html
<!DOCTYPE html>
<html lang="en">
<head>
<meta charset="utf-8">
<title>Ferncrest Dental, LLC — Business Card</title>
<link href="https://fonts.googleapis.com/css2?family=Lato:wght@400;700&display=swap" rel="stylesheet">
<style>
  :root {
    --page-bg: #e6eaec;
    --card-bg: #ffffff;
    --green: #5ba23c;
    --lime: #a8cf3a;
    --ink: #2f2f2f;
    --ink-soft: #444444;
    --rule: #3a3a3a;
  }
  * { box-sizing: border-box; margin: 0; padding: 0; }
  html, body {
    width: 1200px; height: 960px; overflow: hidden;
    background: var(--page-bg);
    font-family: "Lato", Arial, sans-serif;
  }
  .sheet {
    width: 1200px; height: 960px;
    display: flex; flex-direction: column;
    align-items: center; justify-content: center; gap: 56px;
  }
  .card {
    position: relative;
    width: 700px; height: 400px;
    background: var(--card-bg);
    box-shadow: 0 6px 20px rgba(0,0,0,0.15);
    overflow: hidden;
  }
  .card-bands {
    position: absolute; left: 0; right: 0; bottom: 0;
  }
  .band-thin { height: 6px; background: var(--lime); }
  .band-gap { height: 7px; background: var(--card-bg); }
  .band-wide { height: 30px; background: var(--green); }

  .brand {
    display: flex; align-items: center; gap: 12px;
  }
  .brand-dot {
    width: 22px; height: 22px; border-radius: 50%;
    background: var(--lime);
  }
  .brand-name {
    font-weight: 400; color: var(--green);
    letter-spacing: 0.5px;
  }

  /* Front */
  .card-front .brand { position: absolute; left: 40px; top: 44px; }
  .card-front .brand-name { font-size: 44px; }
  .holder-name {
    position: absolute; left: 40px; top: 196px;
    font-size: 34px; font-weight: 400; color: var(--ink);
  }
  .holder-rule {
    position: absolute; left: 40px; right: 40px; top: 248px;
    height: 1.5px; background: var(--rule);
  }
  .contact-list {
    position: absolute; left: 40px; top: 272px;
    list-style: none; display: flex; flex-direction: column; gap: 10px;
  }
  .contact-item {
    display: flex; align-items: center; gap: 14px;
    font-size: 19px; color: var(--ink-soft);
  }
  .contact-icon { width: 18px; height: 18px; flex: none; }
  .address {
    position: absolute; right: 40px; top: 268px;
    display: flex; gap: 10px; align-items: flex-start;
    font-size: 16px; color: var(--ink-soft); line-height: 1.5;
    font-style: normal;
  }

  /* Back */
  .card-back .brand {
    position: absolute; left: 0; right: 0; top: 150px;
    justify-content: center;
  }
  .card-back .brand-name { font-size: 54px; }
  .card-back .brand-dot { width: 28px; height: 28px; }
</style>
</head>
<body>
<main class="sheet">
  <section class="card card-front" aria-label="Business card front">
    <div class="brand">
      <span class="brand-dot"></span>
      <span class="brand-name">Ferncrest Dental</span>
    </div>
    <h1 class="holder-name">Dr. Lorna Pettigrew</h1>
    <div class="holder-rule"></div>
    <ul class="contact-list">
      <li class="contact-item">
        <svg class="contact-icon" viewBox="0 0 24 24" aria-hidden="true"><path fill="#5ba23c" d="M6.6 10.8a15.1 15.1 0 0 0 6.6 6.6l2.2-2.2a1 1 0 0 1 1-.25 11.4 11.4 0 0 0 3.6.57 1 1 0 0 1 1 1V20a1 1 0 0 1-1 1A17 17 0 0 1 3 4a1 1 0 0 1 1-1h3.5a1 1 0 0 1 1 1c0 1.25.2 2.45.57 3.57a1 1 0 0 1-.25 1z"/></svg>
        610-555-0193
      </li>
      <li class="contact-item">
        <svg class="contact-icon" viewBox="0 0 24 24" aria-hidden="true"><rect x="2" y="5" width="20" height="14" rx="2" fill="#5ba23c"/><path d="M3 6l9 7 9-7" fill="none" stroke="#fff" stroke-width="1.8"/></svg>
        ferncrestdental.office@examplemail.test
      </li>
    </ul>
    <address class="address">
      <svg class="contact-icon" viewBox="0 0 24 24" aria-hidden="true"><path fill="#5ba23c" d="M12 2a7 7 0 0 0-7 7c0 5 7 13 7 13s7-8 7-13a7 7 0 0 0-7-7zm0 9.5A2.5 2.5 0 1 1 12 6.5a2.5 2.5 0 0 1 0 5z"/></svg>
      <span>2871 Marlowe Street<br>Bethlehem, PA 18093</span>
    </address>
    <div class="card-bands">
      <div class="band-thin"></div>
      <div class="band-gap"></div>
      <div class="band-wide"></div>
    </div>
  </section>

  <section class="card card-back" aria-label="Business card back">
    <div class="brand">
      <span class="brand-dot"></span>
      <span class="brand-name">Ferncrest Dental</span>
    </div>
    <div class="card-bands">
      <div class="band-thin"></div>
      <div class="band-gap"></div>
      <div class="band-wide"></div>
    </div>
  </section>
</main>
</body>
</html>
```